Tobin's Butter dairy product for export market

We are starting a new brand for our butter range. We are looking for a premimum branding with family values. The product should be elligent and simle and easy for consumers to choose and easy for chefs,

A samples of our current brand and packing details in on the pack
target markets , China, Hong Kong, Asia, middle east
products will be sold in different size starting from small portion eg 7g to 1kg food service pack
product will be sold in 2 varients salted and unsalted

Target Market(s)

Australian Market and export market

Industry/Entity Type

Product

Colors
9bcb3c
fbed22

Requirements
Must have
• Pure butter
• packed in Australia
• nice fresh modern simple design
Nice to have
• Colours gold , green or any other suggestions welcome.
Should not have
• Any third party pictures of butter etc..

```html
<!DOCTYPE html>
<html lang="en">
<head>
<meta charset="utf-8">
<title>Tobin's Pure Butter – 1 kg Carton Dieline</title>
<link rel="stylesheet" href="https://fonts.googleapis.com/css2?family=Oswald:wght@300;500&family=Montserrat:wght@700&family=Roboto+Condensed:wght@700&display=swap">
<style>
  :root {
    --butter-yellow: #fbed7a;
    --bright-yellow: #fbed22;
    --leaf-green: #9bcb3c;
    --panel-green: #6cc065;
    --deep-green: #1f6b2e;
    --burst-green: #8fcf6a;
    --die-line: #3bb0a0;
    --date-blue: #1b9fc9;
    --white: #ffffff;
  }
  * { margin: 0; padding: 0; box-sizing: border-box; }
  html, body { width: 964px; height: 1200px; overflow: hidden; background: var(--butter-yellow); }
  .carton {
    position: relative; width: 964px; height: 1200px; overflow: hidden;
    background:
      radial-gradient(ellipse 60% 48% at 50% 50%, #5cb95a 0%, #8fce5a 45%, var(--butter-yellow) 100%);
  }
  .die-lines { position: absolute; inset: 0; }

  .top-flap { position: absolute; left: 163px; top: 0; width: 635px; height: 159px; }
  .date-code {
    position: absolute; left: 0; right: 0; top: 92px; text-align: center;
    font: 500 30px/1 "Oswald", sans-serif; color: var(--date-blue);
    letter-spacing: 1px; transform: rotate(180deg);
  }

  .back-panel {
    position: absolute; left: 163px; top: 159px; width: 635px; height: 297px;
    background: var(--panel-green);
  }
  .info-box {
    position: absolute; top: 20px; height: 258px; background: var(--butter-yellow);
    display: flex; align-items: center; justify-content: center;
    font: 500 20px/1 "Oswald", sans-serif; color: #333; letter-spacing: 1px;
  }
  .info-box span { transform: rotate(180deg); }
  .nutrition-box { left: 17px; width: 275px; }
  .barcode-box { left: 439px; width: 178px; }
  .brand-literature {
    position: absolute; left: 292px; width: 147px; top: 120px; text-align: center;
    font: 500 17px/1.15 "Oswald", sans-serif; color: #2a3a2a; letter-spacing: 1px;
    transform: rotate(180deg);
  }

  .front-panel {
    position: absolute; left: 163px; width: 635px; height: 287px; overflow: hidden;
    background: radial-gradient(circle at 42% 55%, var(--burst-green) 0%, var(--panel-green) 70%);
  }
  .front-panel.upper { top: 456px; }
  .front-panel.lower { top: 746px; }
  .mascot {
    position: absolute; left: 80px; top: 106px; width: 150px; height: 138px;
    border-radius: 40% 30% 45% 35%;
    background: radial-gradient(circle at 50% 45%, var(--deep-green) 0%, var(--deep-green) 36%, var(--white) 38%, #f2f7ee 100%);
  }
  .brand-name {
    position: absolute; left: 170px; top: 18px;
    font: 500 66px/1.1 "Oswald", sans-serif; color: var(--white); letter-spacing: 1px;
  }
  .product-word {
    position: absolute; left: 278px; top: 104px;
    font: 300 66px/1 "Oswald", sans-serif; color: var(--bright-yellow); letter-spacing: 2px;
  }
  .rule { position: absolute; left: 262px; top: 183px; width: 244px; height: 3px; background: var(--white); }
  .variant {
    position: absolute; left: 322px; top: 205px;
    font: 700 27px/1 "Montserrat", sans-serif; color: var(--white); letter-spacing: 1px;
  }
  .origin, .net-weight {
    position: absolute; top: 252px;
    font: 700 19px/1 "Roboto Condensed", sans-serif; color: var(--white);
  }
  .origin { left: 16px; }
  .net-weight { right: 10px; }

  .side-panel {
    position: absolute; left: 798px; top: 456px; width: 166px; height: 287px;
    background: radial-gradient(circle at 40% 50%, var(--burst-green), var(--panel-green) 75%);
  }
  .side-lockup {
    position: absolute; left: 50%; top: 50%; width: 230px; transform: translate(-50%, -50%) rotate(-90deg);
    display: flex; align-items: center; gap: 8px;
  }
  .side-mascot { width: 46px; height: 52px; border-radius: 45%; transform: rotate(90deg);
    background: radial-gradient(circle, var(--deep-green) 40%, var(--white) 43%); }
  .side-name { font: 500 30px/1 "Oswald", sans-serif; color: var(--white); }
  .side-word { font: 300 30px/1 "Oswald", sans-serif; color: var(--bright-yellow); }
  .side-variant { font: 700 11px/1 "Montserrat", sans-serif; color: var(--white); }
</style>
</head>
<body>
<main class="carton">
  <svg class="die-lines" width="964" height="1200" viewBox="0 0 964 1200" aria-hidden="true" fill="none" stroke="var(--die-line)" stroke-width="1">
    <line x1="163" y1="0" x2="163" y2="1200"/>
    <line x1="798" y1="0" x2="798" y2="1200"/>
    <line x1="0" y1="159" x2="964" y2="159"/>
    <line x1="0" y1="456" x2="964" y2="456"/>
    <line x1="0" y1="743" x2="964" y2="743"/>
    <line x1="0" y1="1039" x2="964" y2="1039"/>
    <path d="M185 0 L225 65 L735 65 L775 0" stroke-dasharray="3 3"/>
    <path d="M185 1200 L225 1148 L735 1148 L775 1200" stroke-dasharray="3 3"/>
    <path d="M0 159 L130 70 M0 456 L130 370 M964 159 L830 70 M964 456 L830 370"/>
    <path d="M125 500 L55 600 L125 700"/>
    <path d="M0 743 L130 830 M0 1039 L130 960 M964 743 L830 830 M964 1039 L830 960"/>
    <path d="M0 1039 L163 1200 M964 1039 L798 1200"/>
  </svg>

  <section class="top-flap">
    <p class="date-code">Date Code Area</p>
  </section>

  <section class="back-panel">
    <div class="info-box nutrition-box"><span>NUTRITION FACTS</span></div>
    <p class="brand-literature">BRAND<br>LITERATURE</p>
    <div class="info-box barcode-box"><span>BARCODE</span></div>
  </section>

  <section class="front-panel upper">
    <div class="mascot" role="img" aria-label="Illustration of a dairy cow over a map of Australia"></div>
    <p class="brand-name">Tobin's Pure</p>
    <p class="product-word">BUTTER</p>
    <div class="rule"></div>
    <p class="variant">UNSALTED</p>
    <p class="origin">Packed in Australia</p>
    <p class="net-weight">1 kg NET</p>
  </section>

  <section class="side-panel">
    <div class="side-lockup">
      <div class="side-mascot" role="img" aria-label="Small dairy cow and Australia map illustration"></div>
      <div>
        <p class="side-name">Tobin's Pure</p>
        <p class="side-word">BUTTER <span class="side-variant">UNSALTED</span></p>
      </div>
    </div>
  </section>

  <section class="front-panel lower">
    <div class="mascot" role="img" aria-label="Illustration of a dairy cow over a map of Australia"></div>
    <p class="brand-name">Tobin's Pure</p>
    <p class="product-word">BUTTER</p>
    <div class="rule"></div>
    <p class="variant">UNSALTED</p>
    <p class="origin">Packed in Australia</p>
    <p class="net-weight">1 kg NET</p>
  </section>
</main>
</body>
</html>
```